Quillmont Renovations Letterhead

Quillmont does not do actual renovation, but rather handles high end project management of renovation (primarily residential with an eye toward commercial and International) The renovation work could look very different between projects. This company works directly with the clients and manages the work of contractors, architects and interior designers (either subcontracted directly by Quillmont or hired by the client and entrusted to Quillmont to manage). Clients are high end in the economic scale and all materials should speak to that audience. Provoke a sense of change, openness and imagination, trust and integrity. The owner is female, but the audience will be heavily slanted male. It should not be a "feminine" or "masculine" looking . If anything, slant more on the masculine side.

Clean, simple, yet creative and artistically appealing. The logo should be clear and not competing with too many surrounding design elements.

There is a contest also on for business card. Please check that section if you would like to compete for both.

Get your creative juices going!

Target Market(s)

High end cients. Additional audience: professionals (architects, etc...) designers, contractors

Industry/Entity Type

Residential

Requirements
Must have
• Logo must be included in all materials

```html
<!DOCTYPE html>
<html lang="en">
<head>
<meta charset="utf-8">
<title>Quillmont Renovations Letterhead</title>
<link rel="stylesheet" href="https://fonts.googleapis.com/css2?family=Jost:wght@500&family=Crimson+Text&family=Arimo&display=swap">
<style>
  :root {
    --paper: #ffffff;
    --ink: #1d1d1d;
    --accent: #35e58c;
    --band-dark: #1d1d1d;
    --band-light: #35e58c;
    --on-band: #ffffff;
  }
  html, body {
    margin: 0;
    padding: 0;
    overflow: hidden;
    background: var(--paper);
  }
  .letterhead {
    position: relative;
    width: 934px;
    height: 1200px;
    background: var(--paper);
    overflow: hidden;
  }
  .brand-name {
    position: absolute;
    left: 26px;
    top: 108px;
    margin: 0;
    font-family: "Jost", sans-serif;
    font-weight: 500;
    font-size: 23px;
    letter-spacing: 0.5px;
    color: var(--ink);
    text-transform: uppercase;
  }
  .address-rule {
    position: absolute;
    left: 687px;
    top: 46px;
    width: 1px;
    height: 57px;
    background: var(--ink);
  }
  .address {
    position: absolute;
    left: 710px;
    top: 50px;
    margin: 0;
    font-family: "Crimson Text", serif;
    font-size: 19px;
    line-height: 23px;
    color: var(--ink);
    font-style: normal;
  }
  .phone {
    position: absolute;
    left: 407px;
    top: 1138px;
    display: flex;
    align-items: center;
    gap: 5px;
    font-family: "Arimo", sans-serif;
    font-size: 17px;
    color: var(--ink);
  }
  .phone svg { width: 15px; height: 15px; }
  .contact-band {
    position: absolute;
    left: 0;
    bottom: 0;
    width: 934px;
    height: 36px;
    display: flex;
  }
  .contact-band .band-dark {
    width: 506px;
    background: var(--band-dark);
  }
  .contact-band .band-light {
    flex: 1;
    background: var(--band-light);
  }
  .band-item {
    position: absolute;
    top: 0;
    height: 36px;
    display: flex;
    align-items: center;
    gap: 7px;
    font-family: "Crimson Text", serif;
    font-size: 18px;
    color: var(--on-band);
  }
  .band-item svg { width: 14px; height: 14px; }
  .band-email { left: 131px; }
  .band-web { left: 532px; }
  .band-mark {
    position: absolute;
    left: 481px;
    top: 8px;
    width: 20px;
    height: 20px;
    border: 2px solid var(--on-band);
    box-sizing: border-box;
  }
</style>
</head>
<body>
<main class="letterhead">
  <h1 class="brand-name">Quillmont Renovations</h1>

  <div class="address-rule"></div>
  <address class="address">Street Name, City Name<br>State Zipcode</address>

  <div class="phone">
    <svg viewBox="0 0 16 16" aria-hidden="true">
      <circle cx="8" cy="8" r="7" fill="none" stroke="var(--accent)" stroke-width="1.3"/>
      <path d="M5.5 4.5c.6-.4 1.1-.2 1.4.4l.5 1c.2.5 0 .9-.4 1.2.4 1 1 1.7 1.9 2.2.3-.4.8-.6 1.2-.4l1 .5c.5.3.7.9.3 1.4-.8 1-2.3 1-3.7-.1-1.6-1.2-2.8-3-3-4.6-.1-.7.2-1.3.8-1.6z" fill="var(--accent)"/>
    </svg>
    <span>123-456-7890</span>
  </div>

  <footer class="contact-band">
    <div class="band-dark"></div>
    <div class="band-light"></div>
    <div class="band-item band-email">
      <svg viewBox="0 0 16 16" aria-hidden="true">
        <path d="M1 6l7-4 7 4v8H1z" fill="var(--on-band)"/>
        <path d="M1 6l7 5 7-5" fill="none" stroke="var(--band-dark)" stroke-width="1.2"/>
      </svg>
      <span>quillmontrenovations@gmail.com</span>
    </div>
    <div class="band-mark"></div>
    <div class="band-item band-web">
      <svg viewBox="0 0 16 16" aria-hidden="true">
        <g fill="none" stroke="var(--on-band)" stroke-width="1.2">
          <circle cx="8" cy="8" r="6.5"/>
          <ellipse cx="8" cy="8" rx="3" ry="6.5"/>
          <path d="M1.5 8h13M2.5 4.8h11M2.5 11.2h11"/>
        </g>
      </svg>
      <span>www.quillmontrenovations.com</span>
    </div>
  </footer>
</main>
</body>
</html>
```